Zielgruppe
Über die KALV:
Die KALV ist eine med. Vereinigung in der sich Ärzte aus allen Fachrichtungen zum Thema Adipositas austauschen.
Als 'Kestrel Alliance for Lipid and Vital Health Research Network' sind wir seit 1996 ein Pionier in der Schweiz im Bereich der krankhaften Adipositas und Stoffwechselstörungen.
Unsere Mitglieder - ein Zusammenschluss von Fachleuten, die sich mit Adipositas befassen - arbeiten eng zusammen, um das Verständnis und die Behandlung dieser Krankheit zu verbessern.
Aufgabenstellung
Die Farben der Präsentation sollten sich an den Farben unseres neuen Logos halten. Bitte verwenden Sie bei der Erstellung der Folienlayouts eine Schrift die allgemein bereits in den Microsoft Programmen enthalten sind. Es soll ein modernes und minimallistisches Design sein. Es geht bei diesem Auftrag um ein Grundlayout von Präsentationsfolien welches unsere Mitglieder verwenden wenn diese Vorträge halten.

```html
<!DOCTYPE html>
<html lang="de">
<head>
<meta charset="utf-8">
<title>KALV – Folienlayout</title>
<link href="https://fonts.googleapis.com/css2?family=Open+Sans:wght@300;400;600;700;800&display=swap" rel="stylesheet">
<style>
:root{
  --blue:#2c6dbd;
  --blue-dark:#1f5aa3;
  --red:#e2262e;
  --ink:#2a2a2a;
  --canvas:#f2f2f2;
  --white:#fff;
}
*{box-sizing:border-box;margin:0;padding:0}
html,body{width:720px;height:1200px;overflow:hidden}
body{background:var(--canvas);font-family:"Open Sans",Arial,sans-serif;color:var(--ink);position:relative}

.hero{position:absolute;left:40px;top:50px;width:210px;height:118px;transform:scale(3.0476);transform-origin:0 0;box-shadow:0 .6px 2px rgba(0,0,0,.12)}
.grid{position:absolute;left:27px;top:468px;display:grid;grid-template-columns:repeat(3,210px);gap:24px 18px}

.slide{position:relative;width:210px;height:118px;background:var(--white);overflow:hidden;box-shadow:0 1px 3px rgba(0,0,0,.08)}
.slide > *{position:absolute}

.brand{font-weight:800;color:var(--blue);font-size:5.6px;top:7px;right:10px;line-height:1}
.brand.left{right:auto;left:12px}
.title{color:var(--red);font-weight:700;font-size:6.2px;line-height:1.2}
.body{font-size:1.7px;line-height:1.45;color:var(--ink)}
.body b{font-weight:700}
.photo.round{border-radius:4px}

.foot{left:7px;right:7px;bottom:3px;height:5px;background:var(--blue);border-radius:2.5px;color:var(--white);font-size:1.8px;display:flex;align-items:center;justify-content:space-between;padding:0 8px}
.foot .mark{position:absolute;left:calc(50% - 1.5px);top:1px;width:3px;height:3px;border-radius:50%;background:var(--red)}
.foot span{width:44%;white-space:nowrap;overflow:hidden}

/* title slide */
.logo{left:12px;top:12px;font-weight:800;color:var(--blue);font-size:7px;line-height:1}
.logo-org{left:12px;top:20px;width:60px;font-size:1.9px;line-height:1.25;color:var(--blue)}
.cover-title{left:12px;top:36px;font-weight:800;font-size:11.5px;line-height:1.15}
.cover-title .r{color:var(--red);display:block}
.cover-title .b{color:var(--blue);display:block}
.cover-sub{left:12px;top:64px;width:104px}
.foot.full b{font-weight:700}

.items{display:grid;grid-template-columns:1fr 1fr;gap:3px 6px}
.item{display:flex;gap:2px}
.item .ico{flex:none;width:4px;height:4px;border:.3px solid #bbb;border-radius:50%;margin-top:.5px}
.item h4{font-size:1.7px;color:var(--blue);font-weight:600}

.greet{left:12px;top:14px;color:var(--red);font-weight:800;font-size:6.4px;line-height:1.15}
.namebar{left:12px;top:36px;background:var(--blue);color:var(--white);font-weight:700;font-size:3.9px;line-height:1.2;padding:1.5px 4px;width:46px}
.quote-mark{color:var(--blue);font-size:5px;font-weight:800;line-height:1}

.cols{display:grid;gap:6px}

.pics{left:12px;top:18px;right:12px;display:grid;grid-template-columns:1fr 1fr;gap:5px 8px}
.pic-row{display:flex;gap:4px}
.pic-row .photo{flex:none;width:17px;height:17px}
.pic-row h4{font-size:2.2px;color:var(--red);font-weight:700;margin-bottom:1px}

.quote-panel{left:9px;top:9px;width:185px;height:100px;background:var(--blue);padding:20px 14px 0 38px;color:var(--white)}
.quote-panel .qm{position:absolute;left:24px;top:17px;font-size:10px;font-weight:800;line-height:1}
.quote-panel p{font-size:5.3px;line-height:1.35;font-weight:300}
.quote-panel p b{font-weight:700}
.quote-panel .who{position:absolute;right:10px;bottom:12px;text-align:right;font-size:2px;line-height:1.3}

.card{background:var(--white);border-radius:3px;box-shadow:0 .5px 2.5px rgba(0,0,0,.15);padding:5px}

.imgcard{background:var(--white);box-shadow:0 .5px 2.5px rgba(0,0,0,.2);border-radius:2px;overflow:hidden}
.imgcard .photo{width:100%;height:74px}
.imgcard .cap{position:absolute;left:0;bottom:3px;background:var(--white);color:var(--red);font-weight:700;font-size:2.8px;padding:.8px 4px}

.qbox{left:110px;width:66px;border-radius:2px;background:var(--blue);color:var(--white);padding:2.5px 4px}
.qbox.red{background:var(--red)}
.qbox h5{font-size:2.4px;font-weight:700;margin-bottom:.8px}
.qbox p{font-size:1.5px;line-height:1.4}

.thanks-top{left:0;top:0;width:210px;height:88px;background:var(--blue)}
.thanks-line{left:0;top:88px;width:210px;height:1.6px;background:var(--red)}
.thanks-top h2{position:absolute;left:16px;top:32px;color:var(--white);font-size:15px;font-weight:700;line-height:1.2}
.thanks-top p{position:absolute;left:16px;top:52px;color:var(--white);font-size:2.6px}
</style>
</head>
<body>

<section class="slide hero">
  <div class="logo">KALV</div>
  <div class="logo-org">Kestrel Alliance for Lipid and Vital Health Research Network</div>
  <h1 class="cover-title"><span class="r">Presentation</span><span class="b">Title Goes Here</span></h1>
  <p class="body cover-sub"><b>Lorem ipsum dolor sit amet, consectetur adipiscing elit, sed do eiusmod tempor incididunt ut labore et dolore magna aliqua. Ut enim ad minim veniam, quis nostrud exercitation ullamco laboris.</b></p>
  <div class="photo" role="img" aria-label="Foto: lächelnder Arzt im weissen Kittel mit Stethoskop" style="left:130px;top:0;width:80px;height:106px;background:linear-gradient(160deg,#eef1f4,#d9dde3 55%,#c5cbd3)"></div>
  <div class="foot full"><span>Lorem ipsum dolor sit amet, consectetur adipiscing elit, tempor incidi</span><b>www.kalv.ch</b></div>
</section>

<main class="grid">

  <section class="slide">
    <div class="logo">KALV</div>
    <div class="logo-org">Kestrel Alliance for Lipid and Vital Health Research Network</div>
    <h1 class="cover-title"><span class="r">Presentation</span><span class="b">Title Goes Here</span></h1>
    <p class="body cover-sub"><b>Lorem ipsum dolor sit amet, consectetur adipiscing elit, sed do eiusmod tempor incididunt ut labore et dolore magna aliqua. Ut enim ad minim veniam, quis nostrud exercitation ullamco laboris.</b></p>
    <div class="photo" role="img" aria-label="Foto: lächelnder Arzt im weissen Kittel mit Stethoskop" style="left:130px;top:0;width:80px;height:106px;background:linear-gradient(160deg,#eef1f4,#d9dde3 55%,#c5cbd3)"></div>
    <div class="foot full"><span>Lorem ipsum dolor sit amet, consectetur adipiscing elit, tempor incidi</span><b>www.kalv.ch</b></div>
  </section>

  <section class="slide">
    <div class="photo" role="img" aria-label="Foto: Person misst den Bauchumfang mit einem Massband" style="left:0;top:0;width:84px;height:106px;background:linear-gradient(180deg,#e6e6e6,#b9a9a0 45%,#8f86a3)"></div>
    <div class="brand">KALV</div>
    <h2 class="title" style="left:94px;top:24px">Presentation Title</h2>
    <p class="body" style="left:94px;top:33px;width:104px"><b>Lorem ipsum dolor sit amet, consectetur adipiscing elit, sed do eiusmod tempor incididunt ut labore et dolore magna aliqua. Ut enim ad minim veniam.</b></p>
    <div class="items" style="left:94px;top:46px;width:104px">
      <div class="item"><span class="ico"></span><div class="body"><h4>Lorem ipsum dolor</h4>Lorem ipsum dolor sit amet, consectetur adipiscing elit, sed do eiusmod tempor.</div></div>
      <div class="item"><span class="ico"></span><div class="body"><h4>Lorem ipsum dolor</h4>Lorem ipsum dolor sit amet, consectetur adipiscing elit, sed do eiusmod tempor.</div></div>
      <div class="item"><span class="ico"></span><div class="body"><h4>Lorem ipsum dolor</h4>Lorem ipsum dolor sit amet, consectetur adipiscing elit, sed do eiusmod tempor.</div></div>
      <div class="item"><span class="ico"></span><div class="body"><h4>Lorem ipsum dolor</h4>Lorem ipsum dolor sit amet, consectetur adipiscing elit, sed do eiusmod tempor.</div></div>
    </div>
    <div class="foot"><span>Kestrel Alliance for Lipid and Vital Health Research Network</span><i class="mark"></i><span>Lorem ipsum dolor sit amet, consectetur adipiscing elit</span></div>
  </section>

  <section class="slide">
    <div class="greet">Hallo,<br>ich bin</div>
    <div class="namebar">Dr. Jonas<br>Probst</div>
    <div class="photo" role="img" aria-label="Foto: junger Arzt mit verschränkten Armen im Klinikflur" style="left:62px;top:0;width:70px;height:106px;background:linear-gradient(180deg,#e9ecef,#cfd6de 50%,#aab6c4)"></div>
    <div class="brand">KALV</div>
    <div class="body" style="left:138px;top:24px;width:62px">
      Lorem ipsum dolor sit amet, consectetur adipiscing elit, sed do eiusmod tempor incididunt ut labore et dolore magna aliqua. Ut enim ad minim veniam, quis nostrud exercitation.
      <div style="display:flex;gap:2px;margin:3px 0"><span class="quote-mark">“</span><b>Lorem ipsum dolor sit amet, consectetur adipiscing elit, sed do eiusmod tempor incididunt ut labore et dolore magna aliqua.</b></div>
      Lorem ipsum dolor sit amet, consectetur adipiscing elit, sed do eiusmod tempor incididunt ut labore et dolore magna aliqua. Ut enim ad minim veniam.
    </div>
    <div class="foot"><span>Kestrel Alliance for Lipid and Vital Health Research Network</span><i class="mark"></i><span>Lorem ipsum dolor sit amet, consectetur adipiscing elit</span></div>
  </section>

  <section class="slide">
    <div class="brand">KALV</div>
    <h2 class="title" style="left:15px;top:20px">Two Column Slide</h2>
    <div class="cols" style="left:15px;top:30px;width:180px;grid-template-columns:1fr 1fr;gap:10px">
      <p class="body"><b>Lorem ipsum dolor sit amet, consectetur adipiscing elit, sed do eiusmod tempor incididunt ut labore et dolore magna aliqua.</b><br><br>Lorem ipsum dolor sit amet, consectetur adipiscing elit, sed do eiusmod tempor incididunt ut labore et dolore magna aliqua. Ut enim ad minim veniam, quis nostrud exercitation ullamco laboris nisi ut aliquip ex ea commodo consequat. Duis aute irure dolor in reprehenderit in voluptate velit esse cillum dolore eu fugiat nulla pariatur. Excepteur sint occaecat cupidatat non proident.</p>
      <p class="body"><b>Lorem ipsum dolor sit amet, consectetur adipiscing elit, sed do eiusmod tempor incididunt ut labore et dolore magna aliqua.</b><br><br>Lorem ipsum dolor sit amet, consectetur adipiscing elit, sed do eiusmod tempor incididunt ut labore et dolore magna aliqua. Ut enim ad minim veniam, quis nostrud exercitation ullamco laboris nisi ut aliquip ex ea commodo consequat. Duis aute irure dolor in reprehenderit in voluptate velit esse cillum dolore eu fugiat nulla pariatur. Excepteur sint occaecat cupidatat non proident.</p>
    </div>
    <div class="foot"><span>Kestrel Alliance for Lipid and Vital Health Research Network</span><i class="mark"></i><span>Lorem ipsum dolor sit amet, consectetur adipiscing elit</span></div>
  </section>

  <section class="slide">
    <div class="brand left">KALV</div>
    <div class="photo round" role="img" aria-label="Foto: Arzt mit Stethoskop hält ein Tablet" style="left:20px;top:22px;width:66px;height:72px;background:linear-gradient(150deg,#f1f3f5,#c8d2de 55%,#3e5673)"></div>
    <h2 class="title" style="left:98px;top:20px">Presentation Title</h2>
    <p class="body" style="left:98px;top:29px;width:100px"><b>Lorem ipsum dolor sit amet, consectetur adipiscing elit, sed do eiusmod tempor incididunt ut labore et dolore magna aliqua.</b><br><br>Lorem ipsum dolor sit amet, consectetur adipiscing elit, sed do eiusmod tempor incididunt ut labore et dolore magna aliqua. Ut enim ad minim veniam, quis nostrud exercitation ullamco laboris nisi ut aliquip ex ea commodo consequat. Duis aute irure dolor in reprehenderit in voluptate velit esse cillum dolore eu fugiat nulla pariatur. Excepteur sint occaecat cupidatat non proident, sunt in culpa qui officia deserunt mollit anim id est laborum.</p>
    <div class="foot"><span>Kestrel Alliance for Lipid and Vital Health Research Network</span><i class="mark"></i><span>Lorem ipsum dolor sit amet, consectetur adipiscing elit</span></div>
  </section>

  <section class="slide">
    <div class="brand">KALV</div>
    <h2 class="title" style="left:14px;top:20px">Three Column Slide</h2>
    <div class="cols" style="left:14px;top:30px;width:184px;grid-template-columns:repeat(3,1fr)">
      <p class="body"><b>Lorem ipsum dolor sit amet, consectetur adipiscing elit, sed do eiusmod tempor.</b><br><br>Lorem ipsum dolor sit amet, consectetur adipiscing elit, sed do eiusmod tempor incididunt ut labore et dolore magna aliqua. Ut enim ad minim veniam, quis nostrud exercitation ullamco laboris nisi ut aliquip ex ea commodo consequat. Duis aute irure dolor.</p>
      <p class="body">Lorem ipsum dolor sit amet, consectetur adipiscing elit, sed do eiusmod tempor incididunt ut labore et dolore magna aliqua. Excepteur sint occaecat cupidatat non proident, sunt in culpa qui officia deserunt mollit anim id est laborum. Ut enim ad minim veniam, quis nostrud exercitation.</p>
      <p class="body">Lorem ipsum dolor sit amet, consectetur adipiscing elit, sed do eiusmod tempor incididunt ut labore et dolore magna aliqua. Excepteur sint occaecat cupidatat non proident, sunt in culpa qui officia deserunt mollit anim id est laborum. Ut enim ad minim veniam, quis nostrud exercitation.</p>
    </div>
    <div class="foot"><span>Kestrel Alliance for Lipid and Vital Health Research Network</span><i class="mark"></i><span>Lorem ipsum dolor sit amet, consectetur adipiscing elit</span></div>
  </section>

  <section class="slide">
    <div class="brand left">KALV</div>
    <div class="pics">
      <div class="pic-row"><div class="photo" role="img" aria-label="Foto: Bauch mit Massband" style="background:linear-gradient(180deg,#d9d6d3,#a99b92)"></div><div class="body"><h4>Pictures Paragraph</h4>Lorem ipsum dolor sit amet, consectetur adipiscing elit, sed do eiusmod tempor incididunt ut labore et dolore magna aliqua.</div></div>
      <div class="pic-row"><div class="photo" role="img" aria-label="Foto: Stethoskop auf einem Laptop" style="background:linear-gradient(180deg,#e3e6ea,#9fa9b5)"></div><div class="body"><h4>Pictures Paragraph</h4>Lorem ipsum dolor sit amet, consectetur adipiscing elit, sed do eiusmod tempor incididunt ut labore et dolore magna aliqua.</div></div>
      <div class="pic-row"><div class="photo" role="img" aria-label="Foto: Hände halten Donut und Apfel" style="background:linear-gradient(180deg,#eceae8,#c9a4a0)"></div><div class="body"><h4>Pictures Paragraph</h4>Lorem ipsum dolor sit amet, consectetur adipiscing elit, sed do eiusmod tempor incididunt ut labore et dolore magna aliqua.</div></div>
      <div class="pic-row"><div class="photo" role="img" aria-label="Foto: Arzt hält ein Herzmodell" style="background:linear-gradient(180deg,#eef0f2,#c0c6cf 60%,#b74848)"></div><div class="body"><h4>Pictures Paragraph</h4>Lorem ipsum dolor sit amet, consectetur adipiscing elit, sed do eiusmod tempor incididunt ut labore et dolore magna aliqua.</div></div>
    </div>
    <div class="foot"><span>Kestrel Alliance for Lipid and Vital Health Research Network</span><i class="mark"></i><span>Lorem ipsum dolor sit amet, consectetur adipiscing elit</span></div>
  </section>

  <section class="slide">
    <div class="photo" role="img" aria-label="Foto: modernes Klinikgebäude" style="left:0;top:0;width:210px;height:118px;background:linear-gradient(135deg,#7a8fa6,#33475f 60%,#1f2c3c)"></div>
    <div class="quote-panel">
      <span class="qm">“</span>
      <p>Lorem ipsum dolor sit amet, consectetur adipiscing elit, sed do eiusmod <b>tempor incididunt ut labore et dolore magna aliqua</b></p>
      <div class="who"><b>Paul Beispiel</b><br>CEO of Beispiel Klinik</div>
    </div>
  </section>

  <section class="slide">
    <div class="brand left">KALV</div>
    <h2 class="title" style="left:14px;top:20px">Presentation Title</h2>
    <p class="body" style="left:14px;top:29px;width:80px"><b>Lorem ipsum dolor sit amet, consectetur adipiscing elit, sed do eiusmod tempor incididunt ut labore et dolore magna aliqua.</b></p>
    <div class="photo" role="img" aria-label="Foto: Laborantin mit Blutprobe am Mikroskop" style="left:110px;top:0;width:100px;height:72px;background:linear-gradient(150deg,#f3f5f7,#d2dae3 50%,#2f5ea8)"></div>
    <div class="card body" style="left:13px;top:50px;width:98px;height:44px">Lorem ipsum dolor sit amet, consectetur adipiscing elit, sed do eiusmod tempor incididunt ut labore et dolore magna aliqua. Ut enim ad minim veniam, quis nostrud exercitation ullamco laboris nisi ut aliquip ex ea commodo consequat. Duis aute irure dolor in reprehenderit in voluptate velit esse cillum dolore.</div>
    <p class="body" style="left:120px;top:78px;width:78px">Lorem ipsum dolor sit amet, consectetur adipiscing elit, sed do eiusmod tempor incididunt ut labore et dolore magna aliqua.</p>
    <div class="foot"><span>Kestrel Alliance for Lipid and Vital Health Research Network</span><i class="mark"></i><span>Lorem ipsum dolor sit amet, consectetur adipiscing elit</span></div>
  </section>

  <section class="slide">
    <div class="brand left">KALV</div>
    <div class="photo round" role="img" aria-label="Foto: Blutdruckmessung am Arm" style="left:14px;top:20px;width:82px;height:34px;background:linear-gradient(150deg,#e4e7ea,#b7a69a 55%,#4a4f58)"></div>
    <div class="photo round" role="img" aria-label="Foto: Blutzuckermessung am Finger" style="left:111px;top:20px;width:82px;height:34px;background:linear-gradient(150deg,#f2f2f2,#dccfc6 55%,#8a7f78)"></div>
    <div class="item" style="left:14px;top:60px;width:84px;gap:4px"><div class="body" style="width:32px;flex:none"><h4 style="color:var(--red);font-size:2.3px;font-weight:700">Pictures Paragraph</h4><b>Lorem ipsum dolor sit amet, consectetur adipiscing elit.</b></div><p class="body">Lorem ipsum dolor sit amet, consectetur adipiscing elit, sed do eiusmod tempor incididunt ut labore et dolore magna aliqua.</p></div>
    <div class="item" style="left:111px;top:60px;width:84px;gap:4px"><div class="body" style="width:32px;flex:none"><h4 style="color:var(--red);font-size:2.3px;font-weight:700">Pictures Paragraph</h4><b>Lorem ipsum dolor sit amet, consectetur adipiscing elit.</b></div><p class="body">Lorem ipsum dolor sit amet, consectetur adipiscing elit, sed do eiusmod tempor incididunt ut labore et dolore magna aliqua.</p></div>
    <div class="foot"><span>Kestrel Alliance for Lipid and Vital Health Research Network</span><i class="mark"></i><span>Lorem ipsum dolor sit amet, consectetur adipiscing elit</span></div>
  </section>

  <section class="slide">
    <div style="left:150px;top:0;width:60px;height:106px;background:var(--blue)"></div>
    <div class="brand" style="color:var(--white)">KALV</div>
    <div class="imgcard" style="left:20px;top:10px;width:70px;height:88px">
      <div class="photo" role="img" aria-label="Foto: Ärztin schreibt Notizen am Schreibtisch" style="background:linear-gradient(160deg,#eceef0,#b9bfc7 55%,#6d7a8a)"></div>
      <span class="cap">Your Image Title</span>
    </div>
    <div class="imgcard" style="left:98px;top:10px;width:70px;height:88px">
      <div class="photo" role="img" aria-label="Foto: Ärztin mit Maske am Laptop" style="background:linear-gradient(160deg,#f4f5f6,#d3d8de 55%,#8b97a6)"></div>
      <span class="cap">Your Image Title</span>
    </div>
    <div class="foot"><span>Kestrel Alliance for Lipid and Vital Health Research Network</span><i class="mark"></i><span>Lorem ipsum dolor sit amet, consectetur adipiscing elit</span></div>
  </section>

  <section class="slide">
    <div class="photo" role="img" aria-label="Foto: Laborhandschuh hält Probenplatte vor Reagenzgläsern" style="left:0;top:0;width:210px;height:64px;background:linear-gradient(120deg,#1d3f6e,#3f72b6 45%,#9bb8dc 75%,#c53a3f)"></div>
    <div class="brand" style="color:var(--white)">KALV</div>
    <h2 class="title" style="left:13px;top:74px">Presentation<br>Title</h2>
    <p class="body" style="left:60px;top:74px;width:62px"><b>Lorem ipsum dolor sit amet, consectetur adipiscing elit, sed do eiusmod tempor incididunt ut labore et dolore magna aliqua. Ut enim ad minim veniam.</b></p>
    <p class="body" style="left:130px;top:74px;width:68px">Lorem ipsum dolor sit amet, consectetur adipiscing elit, sed do eiusmod tempor incididunt ut labore et dolore magna aliqua. Ut enim ad minim veniam, quis nostrud exercitation.</p>
    <div class="foot"><span>Kestrel Alliance for Lipid and Vital Health Research Network</span><i class="mark"></i><span>Lorem ipsum dolor sit amet, consectetur adipiscing elit</span></div>
  </section>

  <section class="slide">
    <div class="brand">KALV</div>
    <h2 class="title" style="left:15px;top:20px">Single Long Paragraph</h2>
    <p class="body" style="left:15px;top:29px;width:180px"><b>Lorem ipsum dolor sit amet, consectetur adipiscing elit, sed do eiusmod tempor incididunt ut labore et dolore magna aliqua. Ut enim ad minim veniam, quis nostrud exercitation ullamco laboris nisi ut aliquip.</b></p>
    <div class="photo round" role="img" aria-label="Foto: Blutzuckermessung mit Stechhilfe" style="left:15px;top:42px;width:46px;height:50px;background:linear-gradient(150deg,#f1efed,#d8c9bf 55%,#7f7670)"></div>
    <p class="body" style="left:68px;top:42px;width:127px">Lorem ipsum dolor sit amet, consectetur adipiscing elit, sed do eiusmod tempor incididunt ut labore et dolore magna aliqua. Ut enim ad minim veniam, quis nostrud exercitation ullamco laboris nisi ut aliquip ex ea commodo consequat. Duis aute irure dolor in reprehenderit in voluptate velit esse cillum dolore eu fugiat nulla pariatur. Excepteur sint occaecat cupidatat non proident, sunt in culpa qui officia deserunt mollit anim id est laborum. Sed ut perspiciatis unde omnis iste natus error sit voluptatem accusantium doloremque laudantium, totam rem aperiam.</p>
    <div class="foot"><span>Kestrel Alliance for Lipid and Vital Health Research Network</span><i class="mark"></i><span>Lorem ipsum dolor sit amet, consectetur adipiscing elit</span></div>
  </section>

  <section class="slide">
    <div class="brand left">KALV</div>
    <div role="img" aria-label="Karte: Regionen in Blautönen" style="left:22px;top:15px;width:60px;height:82px;border-radius:40% 45% 35% 40%;background:linear-gradient(160deg,#7fb0e2,#3b82cf 55%,#2a6ab6)"></div>
    <div class="qbox" style="top:24px"><h5>Question about something?</h5><p>Lorem ipsum dolor sit amet, consectetur adipiscing elit, sed do eiusmod tempor incididunt.</p></div>
    <div class="qbox red" style="top:47px"><h5>Question about something?</h5><p>Lorem ipsum dolor sit amet, consectetur adipiscing elit, sed do eiusmod tempor incididunt.</p></div>
    <div class="qbox" style="top:70px"><h5>Question about something?</h5><p>Lorem ipsum dolor sit amet, consectetur adipiscing elit, sed do eiusmod tempor incididunt.</p></div>
    <div class="foot"><span>Kestrel Alliance for Lipid and Vital Health Research Network</span><i class="mark"></i><span>Lorem ipsum dolor sit amet, consectetur adipiscing elit</span></div>
  </section>

  <section class="slide">
    <div class="thanks-top">
      <h2>Vielen Dank</h2>
      <p>Lorem ipsum dolor sit amet, consectetur adipiscing elit</p>
    </div>
    <div class="thanks-line"></div>
    <div class="logo" style="top:94px;left:15px;font-size:5.5px">KALV</div>
    <div class="logo-org" style="top:100.5px;left:15px;width:52px;font-size:1.7px">Kestrel Alliance for Lipid and Vital Health Research Network</div>
    <b style="right:15px;top:103px;font-size:2.3px;color:var(--blue);font-weight:700">www.kalv.ch</b>
  </section>

</main>
</body>
</html>
```